Flyer for The Quiet Bloom Gathering

I am launching my new offering in my business at an event next Sunday where I have a booth and need a flyer advertising the offering, so the flyer needs to stand out for other practitioners that will also be there on the day offering there services.
This flyer is also what I will use for marketing on social media as well as on the day of the event. See the link below to the offering
http://sarahlindqvist.com.au/quiet-bloom-gathering/

Target Market(s)

Women with body image issues - age range 25 - 65
Women with issues around food such as binge eating, emotional eating, eating disorders.

Industry/Entity Type

Health And Wellness

Font styles to use
Serif
Sans Serif
Script

Colors
f9d9e8
85cae6
cee9f5
fee18a
ffffff
eea4c8

Requirements
Must have
• Colours matching my overall website at sarahlindqvist.com.au - pinks, light blue, gold, white
• Imagery similiar to my Instagram, see below https://www.instagram.com/riverstonecarexy/
• - soft, warm, welcoming, nurturing, safe, inviting - see image on sales page for inspiration
• contact details
Should not have
• harsh dark colours or harsh lines

```html
<!DOCTYPE html>
<html lang="en">
<head>
<meta charset="UTF-8">
<title>The Quiet Bloom Gathering</title>
<link rel="stylesheet" href="https://fonts.googleapis.com/css2?family=Montserrat:wght@700;800&family=Open+Sans:wght@400;600;700&family=Pacifico&display=swap">
<style>
  :root {
    --pink-soft: #f9d9e8;
    --pink: #eea4c8;
    --pink-deep: #e3649f;
    --blue: #85cae6;
    --blue-pale: #cee9f5;
    --blue-mist: #e4f3fa;
    --gold: #fee18a;
    --white: #ffffff;
    --ink: #353a44;
    --ink-body: #3f4650;
    --lilac: #c9a7d8;
  }
  html, body {
    margin: 0;
    padding: 0;
    overflow: hidden;
    background: var(--white);
  }
  .flyer {
    position: relative;
    width: 847px;
    height: 1200px;
    overflow: hidden;
    background: var(--blue-pale);
    font-family: "Open Sans", Arial, sans-serif;
    color: var(--ink-body);
  }
  .hero-image {
    position: absolute;
    left: 0; top: 0;
    width: 847px; height: 329px;
    background:
      radial-gradient(ellipse at 20% 40%, rgba(255,235,245,0.9), rgba(255,235,245,0) 55%),
      radial-gradient(ellipse at 75% 20%, rgba(214,182,230,0.9), rgba(214,182,230,0) 60%),
      linear-gradient(160deg, #f3cfe2 0%, #e2b4d4 45%, var(--lilac) 100%);
  }
  .portrait {
    position: absolute;
    left: 515px; top: 168px;
    width: 271px; height: 271px;
    border-radius: 50%;
    border: 6px solid var(--white);
    background: linear-gradient(150deg, #f6ece6 0%, #e9d8cf 50%, #d98aa6 100%);
    box-shadow: 0 4px 14px rgba(120, 80, 110, 0.25);
    z-index: 3;
  }
  .title-band {
    position: absolute;
    left: 0; top: 329px;
    width: 847px; height: 200px;
    background: linear-gradient(180deg, #9fd5ec 0%, var(--blue) 100%);
    border-top: 4px solid var(--white);
    box-sizing: border-box;
  }
  .title {
    position: absolute;
    left: 36px; top: 20px;
    margin: 0;
    font-family: "Montserrat", Arial, sans-serif;
    font-weight: 800;
    font-size: 48px;
    line-height: 64px;
    color: var(--ink);
    letter-spacing: 0.5px;
  }
  .title-line { display: block; }
  .title-script {
    font-family: "Pacifico", cursive;
    font-weight: 400;
    font-size: 50px;
    color: var(--pink-deep);
    letter-spacing: 0;
    text-shadow: 2px 2px 0 var(--white);
    margin-right: 10px;
    position: relative;
    top: 2px;
  }
  .content {
    position: absolute;
    left: 0; top: 529px;
    width: 847px; height: 592px;
    background: linear-gradient(180deg, var(--blue-mist) 0%, var(--blue-pale) 100%);
    border-top: 3px solid var(--white);
    box-sizing: border-box;
  }
  .invitation {
    margin: 0 40px;
    text-align: center;
    font-size: 28px;
    line-height: 36px;
    font-weight: 400;
    color: #2e3440;
  }
  .invitation strong { font-weight: 700; }
  .divider {
    display: block;
    margin: 8px auto 0;
  }
  .body-copy {
    margin: 0 36px;
    font-size: 17px;
    line-height: 28px;
    font-weight: 600;
    color: var(--ink-body);
  }
  .lead { margin-top: 10px; }
  .offer-intro { margin-top: 21px; }
  .benefits {
    list-style: none;
    margin: 6px 36px 0;
    padding: 0;
    font-size: 17px;
    line-height: 28px;
    font-weight: 600;
    color: var(--ink-body);
  }
  .benefits li {
    position: relative;
    padding-left: 24px;
    margin-bottom: 8px;
  }
  .benefits li::before {
    content: "";
    position: absolute;
    left: 4px; top: 10px;
    width: 8px; height: 8px;
    border-radius: 50%;
    background: var(--ink-body);
  }
  .investment { margin-top: 14px; }
  .cta-band {
    position: absolute;
    left: 0; top: 1121px;
    width: 847px; height: 79px;
    background: var(--blue);
    border-top: 3px solid var(--white);
    box-sizing: border-box;
    text-align: center;
  }
  .cta {
    margin: 0;
    font-family: "Montserrat", Arial, sans-serif;
    font-weight: 800;
    font-size: 26px;
    line-height: 76px;
    color: var(--ink);
    letter-spacing: 0.5px;
  }
</style>
</head>
<body>
<main class="flyer">
  <div class="hero-image" role="img" aria-label="Soft pink and lilac photograph of a woman resting peacefully with eyes closed"></div>
  <div class="portrait" role="img" aria-label="Photograph of the practitioner sitting on a sofa with a small dog and a journal"></div>

  <header class="title-band">
    <h1 class="title">
      <span class="title-line">THE QUIET</span>
      <span class="title-line"><span class="title-script">Bloom</span>GATHERING</span>
    </h1>
  </header>

  <section class="content">
    <p class="invitation">
      It’s time to make a commitment....<br>
      It’s time for <strong>YOU</strong>, to <strong>SHOW UP</strong> for <strong>YOU</strong>.....<br>
      It’s time to truly let go.......and finally heal,<br>
      and find the peace that you so long for...
    </p>
    <svg class="divider" width="164" height="4" viewBox="0 0 164 4" aria-hidden="true">
      <line x1="0" y1="2" x2="164" y2="2" stroke="#2e3440" stroke-width="3" stroke-dasharray="14 7"/>
    </svg>

    <p class="body-copy lead">I am inviting 10 women only into this six-week healing experience, as I personally know, that when we share our stories, it opens our hearts for other people to share their stories. It gives us the sense we are not alone in our journey’s.</p>

    <p class="body-copy offer-intro">The women that come on this six-week journey will receive;</p>
    <ul class="benefits">
      <li>One 90mins one on one coaching sessionwith me (which for the women that have attended the Friday circle previously, can be done before this healing circle begins);</li>
      <li>Private Members Group to continue support outside of the circle</li>
      <li>Homework outside of circle to support your healing</li>
      <li>Journal and other small gifts weekly</li>
    </ul>

    <p class="body-copy investment">The financial investment in YOU, is $XX for the six weeks. For the women that have attended the Friday night, Gentle Rose Sister Circle, you will receive a discount of $100, taking the price to $XX.</p>
  </section>

  <footer class="cta-band">
    <p class="cta">ARE YOU READY?</p>
  </footer>
</main>
</body>
</html>
```